Business card design for industrial spray painting - startup business

Design the layout of our new business card using the logo we have provided.

We want the card to be matt black in colour.

We only want our logo and slogan on the face side.

Because the card is black we would like the slogan WE PAINT ANYTHING! to be in white.

We want our information on the rear side.

I would like my name in blue matching the blue in the logo.

The remainder of the information should be in grey to match the grey in the logo.

The overall finish should look minimal, clean and slick.

Our business is industrlal and of a masculine nature.

Target Market(s)

industrial and mining companies

Contact Information for Business Card

(front of card – matt black)
insert logo here:
insert this tag line: WE PAINT ANYTHING!

--------------------------------------------------------------------------------------------------------------

(back of card – matt black)
Dorian Kestle
Paint and Coatings Specialist
47 Millbrook Avenue, Bayswater WA 6053
M: +61 437 281 914
T: +61 8 555 7318
E: dorian@coatlynx.co
W: www.coatlynx.co

Font styles to use
Sans Serif

Colors
000000
0455a3

Requirements
Must have
• clean, slick minimalist look. Masculine as we deal mostly with industrial spray painting

```html
<!DOCTYPE html>
<html lang="en">
<head>
<meta charset="utf-8">
<title>Coatlynx Business Card</title>
<link href="https://fonts.googleapis.com/css2?family=Oswald:wght@600&family=Roboto+Condensed:wght@400;500&display=swap" rel="stylesheet">
<style>
  :root {
    --backdrop: #808080;
    --card-black: #000000;
    --brand-blue: #1b6fbf;
    --name-blue: #0f5fae;
    --brand-grey: #8c8c8c;
    --text-grey: #9a9a9a;
    --slogan-white: #ffffff;
  }
  * { margin: 0; padding: 0; box-sizing: border-box; }
  html, body { width: 1200px; height: 1200px; overflow: hidden; }
  body {
    background: var(--backdrop);
    position: relative;
    font-family: "Roboto Condensed", sans-serif;
  }
  .card {
    position: absolute;
    left: 241px;
    width: 719px;
    height: 421px;
    background: var(--card-black);
  }
  .card--front { top: 138px; }
  .card--back { top: 624px; }

  .brand {
    position: absolute;
    display: flex;
    align-items: center;
    gap: 14px;
    color: var(--brand-blue);
    font-family: "Roboto Condensed", sans-serif;
    font-weight: 500;
    letter-spacing: 0.06em;
  }
  .brand__square { background: var(--brand-blue); flex: none; }
  .brand--front {
    left: 0; right: 0; top: 176px;
    justify-content: center;
    font-size: 58px;
    line-height: 1;
  }
  .brand--front .brand__square { width: 40px; height: 40px; }
  .brand--back {
    left: 30px; width: 400px; top: 160px;
    justify-content: center;
    font-size: 38px;
    line-height: 1;
  }
  .brand--back .brand__square { width: 28px; height: 28px; }

  .slogan {
    position: absolute;
    left: 0; right: 0; top: 362px;
    text-align: center;
    color: var(--slogan-white);
    font-family: "Oswald", sans-serif;
    font-weight: 600;
    font-size: 29px;
    line-height: 1.2;
    letter-spacing: 0.01em;
  }

  .address {
    position: absolute;
    right: 330px;
    top: 263px;
    color: var(--text-grey);
    font-size: 19px;
    white-space: nowrap;
  }
  .divider {
    position: absolute;
    left: 405px;
    top: 129px;
    width: 2px;
    height: 163px;
    background: var(--name-blue);
  }
  .contact {
    position: absolute;
    left: 428px;
    top: 128px;
  }
  .contact__name {
    color: var(--name-blue);
    font-size: 27px;
    font-weight: 400;
    line-height: 1.2;
  }
  .contact__role {
    color: var(--text-grey);
    font-size: 16px;
    margin-top: 2px;
  }
  .contact__list {
    list-style: none;
    margin-top: 14px;
  }
  .contact__item {
    display: flex;
    align-items: center;
    height: 25px;
    color: var(--text-grey);
    font-size: 19px;
  }
  .contact__icon {
    width: 14px; height: 14px;
    margin-right: 12px;
    flex: none;
  }
</style>
</head>
<body>
  <section class="card card--front" aria-label="Card front">
    <div class="brand brand--front">
      <span class="brand__square"></span>
      <span class="brand__name">COATLYNX</span>
    </div>
    <p class="slogan">WE PAINT ANYTHING!</p>
  </section>

  <section class="card card--back" aria-label="Card back">
    <div class="brand brand--back">
      <span class="brand__square"></span>
      <span class="brand__name">COATLYNX</span>
    </div>
    <p class="address">47 Millbrook Avenue, Bayswater WA 6053</p>
    <div class="divider"></div>
    <div class="contact">
      <h1 class="contact__name">DORIAN KESTLE</h1>
      <p class="contact__role">Paint and Coatings Specialist</p>
      <ul class="contact__list">
        <li class="contact__item">
          <svg class="contact__icon" viewBox="0 0 14 14" aria-hidden="true"><rect x="4" y="1" width="7" height="12" rx="1.3" fill="none" stroke="var(--name-blue)" stroke-width="1.4" transform="rotate(15 7 7)"/></svg>
          +61 437 281 914
        </li>
        <li class="contact__item">
          <svg class="contact__icon" viewBox="0 0 14 14" aria-hidden="true"><rect x="1" y="2" width="3" height="10" rx="1" fill="var(--name-blue)"/><rect x="5" y="3" width="8" height="9" rx="1" fill="var(--name-blue)"/><rect x="7" y="5" width="4" height="1.5" fill="#000"/><rect x="7" y="8" width="4" height="1.5" fill="#000"/></svg>
          +61 8 555 7318
        </li>
        <li class="contact__item">
          <svg class="contact__icon" viewBox="0 0 14 14" aria-hidden="true"><rect x="1" y="3" width="12" height="8" fill="var(--name-blue)"/><path d="M1 3 L7 8 L13 3" fill="none" stroke="#000" stroke-width="1"/></svg>
          dorian@coatlynx.co
        </li>
        <li class="contact__item">
          <svg class="contact__icon" viewBox="0 0 14 14" aria-hidden="true"><g fill="none" stroke="var(--name-blue)" stroke-width="1.2"><circle cx="7" cy="7" r="5.6"/><ellipse cx="7" cy="7" rx="2.4" ry="5.6"/><line x1="1.4" y1="7" x2="12.6" y2="7"/></g></svg>
          www.coatlynx.co
        </li>
      </ul>
    </div>
  </section>
</body>
</html>
```